Clear Plastic Card Design

I am looking to have a business card designed from my logo icon. I am looking to match the style of a different business card I have attached in the files.
Looking for a card that is plastic, with layers of transparency in the shape of my logo icon (also attached in the files) - not a circle like the other card. The winning design will incorporate the red icon logo on the front and back and include the charity's name, "Lanterns for the Weary" in the same or similar font, as well as an email and phone number. For now, use the email: email@lanternsfortheweary.org and the phone number 555-318-4072.
We like how the sample business card has transparency, partial and full opacity layers and a matching color scheme. Files will need to be in vector so that our business card printing company can work with it.
UPDATE:
We've some excellent designs in, thank you everyone! I got an early review from the owner, and he requested a minor redirect to find his perfect design. He wants the design to stand out by NOT being a rectangle. Try instead a circle, square, or best yet - something that falls in the outline of the logo icon, either fully or partially. Thank you, everyone!
Contact Information for Business Card
Lanterns for the Weary text should be incorporated as well as a phone and email.
Look and feel

```html
<!DOCTYPE html>
<html lang="en">
<head>
<meta charset="UTF-8">
<title>Lanterns for the Weary — Square Business Card</title>
<link rel="stylesheet" href="https://fonts.googleapis.com/css2?family=Montserrat:wght@400;700&display=swap">
<style>
  :root {
    --backdrop: #e8e8e8;
    --card: #ffffff;
    --flame: #ee4827;
    --peach: #fce6de;
    --blush: #edb0b0;
    --ink: #1a1a1a;
    --mark: #e0322f;
    --on-flame: #ffffff;
  }
  * { margin: 0; padding: 0; box-sizing: border-box; }
  html, body {
    width: 1200px;
    height: 1200px;
    overflow: hidden;
    background: var(--backdrop);
    font-family: "Montserrat", Arial, sans-serif;
  }
  .card {
    position: absolute;
    left: 344px;
    width: 512px;
    height: 512px;
    background: var(--card);
    overflow: hidden;
  }
  .card--front { top: 66px; }
  .card--back { top: 622px; }

  .card__shapes {
    position: absolute;
    inset: 0;
    width: 100%;
    height: 100%;
  }
  .shape--flame { fill: var(--flame); }
  .shape--peach { fill: var(--peach); }
  .shape--blush { fill: var(--blush); }

  .contact {
    position: absolute;
    left: 46px;
    top: 58px;
    color: var(--on-flame);
  }
  .contact__name {
    font-weight: 700;
    font-size: 23px;
    line-height: 30px;
    letter-spacing: 0.4px;
    text-transform: uppercase;
  }
  .contact__list {
    list-style: none;
    margin-top: 22px;
  }
  .contact__item {
    display: flex;
    align-items: center;
    gap: 12px;
    font-size: 18px;
    font-weight: 400;
    height: 38px;
    white-space: nowrap;
  }
  .contact__icon {
    width: 17px;
    height: 17px;
    fill: var(--on-flame);
    flex: none;
  }

  .wordmark {
    position: absolute;
    display: flex;
    align-items: center;
    gap: 16px;
  }
  .wordmark__square {
    background: var(--mark);
    flex: none;
  }
  .wordmark__name {
    font-weight: 400;
    color: var(--ink);
    line-height: 1.15;
    white-space: nowrap;
  }
  .card--front .wordmark {
    right: 34px;
    bottom: 38px;
  }
  .card--front .wordmark__square { width: 40px; height: 40px; }
  .card--front .wordmark__name { font-size: 28px; }
  .card--back .wordmark {
    left: 50%;
    top: 50%;
    transform: translate(-50%, -50%);
  }
  .card--back .wordmark__square { width: 50px; height: 50px; }
  .card--back .wordmark__name { font-size: 35px; }
</style>
</head>
<body>
  <section class="card card--front" aria-label="Card front">
    <svg class="card__shapes" viewBox="0 0 512 512" aria-hidden="true">
      <path class="shape--peach" d="M468 0 H512 V150 C490 130 470 90 466 45 C465 25 466 10 468 0 Z"/>
      <path class="shape--blush" d="M0 512 V470 C15 432 40 416 80 416 C140 418 190 430 215 450 C228 462 230 495 230 512 Z"/>
      <path class="shape--flame" d="M0 0 H385 C450 40 462 160 444 222 C424 280 300 302 0 342 Z"/>
    </svg>

    <div class="contact">
      <h1 class="contact__name">Lanterns for<br>the Weary</h1>
      <ul class="contact__list">
        <li class="contact__item">
          <svg class="contact__icon" viewBox="0 0 24 24" aria-hidden="true">
            <path d="M6.6 10.8c1.4 2.8 3.8 5.1 6.6 6.6l2.2-2.2c.3-.3.7-.4 1-.2 1.1.4 2.3.6 3.6.6.6 0 1 .4 1 1V20c0 .6-.4 1-1 1C10.6 21 3 13.4 3 4c0-.6.4-1 1-1h3.5c.6 0 1 .4 1 1 0 1.3.2 2.5.6 3.6.1.3 0 .7-.2 1z"/>
          </svg>
          <span>555-318-4072</span>
        </li>
        <li class="contact__item">
          <svg class="contact__icon" viewBox="0 0 24 24" aria-hidden="true">
            <path d="M3 5h18c.6 0 1 .4 1 1v12c0 .6-.4 1-1 1H3c-.6 0-1-.4-1-1V6c0-.6.4-1 1-1zm9 7.5L20.5 7h-17z"/>
          </svg>
          <span>email@lanternsfortheweary.org</span>
        </li>
      </ul>
    </div>

    <div class="wordmark">
      <span class="wordmark__square" aria-hidden="true"></span>
      <span class="wordmark__name">Lanterns for<br>the Weary</span>
    </div>
  </section>

  <section class="card card--back" aria-label="Card back">
    <div class="wordmark">
      <span class="wordmark__square" aria-hidden="true"></span>
      <span class="wordmark__name">Lanterns for<br>the Weary</span>
    </div>
  </section>
</body>
</html>
```